A restaurant needs a new design for menu and presentation flyers.

The name of the restaurant located in Germany is ,, GASTSTÄTTE ZUM TALHAHN" . It means RESTAURANT THE DALE ROOSTER. I attached two photos for reference to see the actual fonts.
I would like to have something close to the fonts we have now. I would like to add a crown representation.Any idea is welcomed.

Target Market(s)

GERMANY

Contact Information for Business Card

Must have ZUM TALHAHN logo.

Requirements
Nice to have
• A crown representation or other symbol who can be representative for our business.
An font close to actual fonts.

```html
<!DOCTYPE html>
<html lang="de">
<head>
<meta charset="utf-8">
<title>Zum Talhahn – Menu &amp; Valentinstag Flyer</title>
<link href="https://fonts.googleapis.com/css2?family=Parisienne&family=Cinzel:wght@400;600&family=Josefin+Sans:wght@400;700&display=swap" rel="stylesheet">
<style>
  :root{
    --stage:#ffffff;
    --cream:#f6f1d6;
    --ink:#1f1f1f;
    --rule:#555555;
    --band:#2a2a2a;
    --wine:#7d1836;
    --wine-line:#f3e6d8;
    --placeholder-ink:#e6dfc3;
    --placeholder-wine:#8a2644;
  }
  *{box-sizing:border-box;margin:0;padding:0}
  html,body{width:1200px;height:1000px;overflow:hidden;background:var(--stage)}
  body{position:relative;font-family:"Josefin Sans",sans-serif}

  .page{position:absolute;top:100px;width:568px;height:803px;overflow:hidden}
  .page--menu{left:20px;background:var(--cream);color:var(--ink)}
  .page--promo{left:618px;width:569px;background:var(--wine);color:var(--wine-line)}
  .page__band{position:absolute;left:0;right:0;bottom:0;height:13px}
  .page--menu .page__band{background:var(--band)}
  .page--promo .page__band{background:var(--cream)}

  /* Header */
  .crest{position:absolute;left:225px;top:20px;width:110px;height:86px;border-radius:10px}
  .flourish{position:absolute;top:55px;height:112px;border-radius:18px}
  .flourish--left{left:70px;width:132px}
  .flourish--right{left:366px;width:132px}
  .page--menu .crest,.page--menu .flourish{background:var(--placeholder-ink)}
  .page--promo .crest,.page--promo .flourish{background:var(--placeholder-wine)}
  .header-rules{position:absolute;left:0;top:0;width:568px;height:210px}
  .brand-name{position:absolute;left:0;right:0;top:112px;text-align:center;
    font-family:"Parisienne",cursive;font-size:52px;font-weight:400;line-height:1}
  .menu-tag{position:absolute;left:235px;top:167px;width:98px;height:31px;
    border:1px solid currentColor;border-top:none;border-radius:0 0 8px 8px;
    font-family:"Cinzel",serif;font-size:19px;text-align:center;line-height:33px;letter-spacing:.5px}

  /* Ribbons */
  .ribbon{position:absolute;height:26px;display:flex;align-items:center;justify-content:center}
  .ribbon svg{position:absolute;inset:0;width:100%;height:100%}
  .ribbon span{position:relative;color:var(--cream);font-family:"Cinzel",serif;font-size:13px;letter-spacing:.5px}

  /* Price lists */
  .price-list{position:absolute;list-style:none}
  .price-list li{display:flex;align-items:baseline;height:22.2px;font-size:12.5px;letter-spacing:.3px}
  .price-list .leader{flex:1;overflow:hidden;white-space:nowrap;margin:0 3px}
  .price-list .leader::before{content:". . . . . . . . . . . . . . . . . . . . . . . . . . . . . . . . . . . . . . . . . . . . . . . . . . . . . . . . . . . . . . .";letter-spacing:.6px}
  .price-list .price{font-weight:700}
  .list--starters{left:58px;top:256px;width:210px}
  .list--mains{left:300px;top:256px;width:212px}
  .list--desserts{left:300px;top:481px;width:212px}
  .list--drinks-a{left:62px;top:665px;width:210px}
  .list--drinks-b{left:294px;top:665px;width:208px}
  .list--drinks-a li,.list--drinks-b li{height:22px}

  .column-rule{position:absolute;left:282px;top:210px;width:1px;height:395px;background:var(--rule)}
  .drinks-frame{position:absolute;left:48px;top:638px;width:472px;height:120px;border:1px solid var(--rule);border-radius:8px}
  .drinks-rule{position:absolute;top:626px;height:1px;background:var(--rule)}

  /* Promo copy */
  .promo-title{position:absolute;left:0;right:0;top:246px;text-align:center;
    font-family:"Parisienne",cursive;font-size:38px;font-weight:400;line-height:1}
  .promo-copy{position:absolute;left:30px;right:30px;text-align:center;font-size:14px;line-height:19px}
  .promo-copy strong{font-weight:700}

  .gallery{position:absolute;left:59px;top:643px;width:456px;height:95px;background:var(--cream);
    display:flex;gap:8px;padding:9px 10px}
  .gallery__photo{flex:1}
  .photo--soup{background:linear-gradient(135deg,#2e2a26,#b8582c 55%,#4f6a2c)}
  .photo--steak{background:linear-gradient(135deg,#3a3230,#7a2e2e 50%,#2b2624)}
  .photo--dessert{background:linear-gradient(135deg,#c9c4c2,#b07a5a 50%,#c02a2a)}
  .promo-rule{position:absolute;left:45px;top:766px;width:480px;height:1px;background:var(--wine-line)}
</style>
</head>
<body>

<!-- Menu page -->
<section class="page page--menu">
  <div class="flourish flourish--left" role="img" aria-label="Scroll flourish ornament"></div>
  <div class="flourish flourish--right" role="img" aria-label="Scroll flourish ornament"></div>
  <div class="crest" role="img" aria-label="Crown emblem illustration"></div>
  <svg class="header-rules" viewBox="0 0 568 210" aria-hidden="true" fill="none" stroke="#555" stroke-width="1">
    <path d="M50 170 H235 M333 170 H518"/>
    <path d="M50 166 H235 M333 166 H518" stroke-width=".6"/>
  </svg>
  <h1 class="brand-name">Zum Talhahn</h1>
  <div class="menu-tag">MENU</div>

  <div class="ribbon" style="left:85px;top:211px;width:150px">
    <svg viewBox="0 0 150 26" preserveAspectRatio="none" aria-hidden="true"><polygon points="0,6 12,6 12,2 138,2 138,6 150,6 144,14 150,22 138,22 138,24 12,24 12,22 0,22 6,14" fill="#1f1f1f"/></svg>
    <span>STARTERS</span>
  </div>
  <div class="ribbon" style="left:325px;top:211px;width:150px">
    <svg viewBox="0 0 150 26" preserveAspectRatio="none" aria-hidden="true"><polygon points="0,6 12,6 12,2 138,2 138,6 150,6 144,14 150,22 138,22 138,24 12,24 12,22 0,22 6,14" fill="#1f1f1f"/></svg>
    <span>MAIN DISH</span>
  </div>
  <div class="ribbon" style="left:330px;top:435px;width:140px">
    <svg viewBox="0 0 150 26" preserveAspectRatio="none" aria-hidden="true"><polygon points="0,6 12,6 12,2 138,2 138,6 150,6 144,14 150,22 138,22 138,24 12,24 12,22 0,22 6,14" fill="#1f1f1f"/></svg>
    <span>DESSERTS</span>
  </div>

  <ul class="price-list list--starters">
    <li>DISH<span class="leader"></span><span class="price">€10</span></li>
    <li>DISH<span class="leader"></span><span class="price">€10</span></li>
    <li>DISH<span class="leader"></span><span class="price">€10</span></li>
    <li>DISH<span class="leader"></span><span class="price">€10</span></li>
    <li>DISH<span class="leader"></span><span class="price">€10</span></li>
    <li>DISH<span class="leader"></span><span class="price">€10</span></li>
    <li>DISH<span class="leader"></span><span class="price">€10</span></li>
    <li>DISH<span class="leader"></span><span class="price">€10</span></li>
    <li>DISH<span class="leader"></span><span class="price">€10</span></li>
    <li>DISH<span class="leader"></span><span class="price">€10</span></li>
    <li>DISH<span class="leader"></span><span class="price">€10</span></li>
    <li>DISH<span class="leader"></span><span class="price">€10</span></li>
    <li>DISH<span class="leader"></span><span class="price">€10</span></li>
    <li>DISH<span class="leader"></span><span class="price">€10</span></li>
    <li>DISH<span class="leader"></span><span class="price">€10</span></li>
    <li>DISH<span class="leader"></span><span class="price">€10</span></li>
  </ul>

  <div class="column-rule"></div>

  <ul class="price-list list--mains">
    <li>DISH<span class="leader"></span><span class="price">€10</span></li>
    <li>DISH<span class="leader"></span><span class="price">€10</span></li>
    <li>DISH<span class="leader"></span><span class="price">€10</span></li>
    <li>DISH<span class="leader"></span><span class="price">€10</span></li>
    <li>DISH<span class="leader"></span><span class="price">€10</span></li>
    <li>DISH<span class="leader"></span><span class="price">€10</span></li>
    <li>DISH<span class="leader"></span><span class="price">€10</span></li>
    <li>DISH<span class="leader"></span><span class="price">€10</span></li>
  </ul>

  <ul class="price-list list--desserts">
    <li>DISH<span class="leader"></span><span class="price">€10</span></li>
    <li>DISH<span class="leader"></span><span class="price">€10</span></li>
    <li>DISH<span class="leader"></span><span class="price">€10</span></li>
    <li>DISH<span class="leader"></span><span class="price">€10</span></li>
    <li>DISH<span class="leader"></span><span class="price">€10</span></li>
    <li>DISH<span class="leader"></span><span class="price">€10</span></li>
  </ul>

  <div class="drinks-rule" style="left:45px;width:170px"></div>
  <div class="drinks-rule" style="left:353px;width:170px"></div>
  <div class="drinks-frame"></div>
  <div class="ribbon" style="left:214px;top:614px;width:140px">
    <svg viewBox="0 0 150 26" preserveAspectRatio="none" aria-hidden="true"><polygon points="0,6 12,6 12,2 138,2 138,6 150,6 144,14 150,22 138,22 138,24 12,24 12,22 0,22 6,14" fill="#1f1f1f"/></svg>
    <span>DRINKS</span>
  </div>

  <ul class="price-list list--drinks-a">
    <li>DRINK<span class="leader"></span><span class="price">€10</span></li>
    <li>DRINK<span class="leader"></span><span class="price">€10</span></li>
    <li>DRINK<span class="leader"></span><span class="price">€10</span></li>
    <li>DRINK<span class="leader"></span><span class="price">€10</span></li>
  </ul>
  <ul class="price-list list--drinks-b">
    <li>DRINK<span class="leader"></span><span class="price">€10</span></li>
    <li>DRINK<span class="leader"></span><span class="price">€10</span></li>
    <li>DRINK<span class="leader"></span><span class="price">€10</span></li>
    <li>DRINK<span class="leader"></span><span class="price">€10</span></li>
  </ul>

  <div class="page__band"></div>
</section>

<!-- Valentine promo page -->
<section class="page page--promo">
  <div class="flourish flourish--left" role="img" aria-label="Scroll flourish ornament"></div>
  <div class="flourish flourish--right" role="img" aria-label="Scroll flourish ornament"></div>
  <div class="crest" role="img" aria-label="Crown emblem illustration"></div>
  <svg class="header-rules" viewBox="0 0 568 210" aria-hidden="true" fill="none" stroke="#f3e6d8" stroke-width="1">
    <path d="M50 170 H235 M333 170 H518"/>
    <path d="M50 166 H235 M333 166 H518" stroke-width=".6"/>
  </svg>
  <h1 class="brand-name">Zum Talhahn</h1>
  <div class="menu-tag">MENU</div>

  <h2 class="promo-title">Liebe Gaste</h2>
  <p class="promo-copy" style="top:304px">Zum Valentistag verlosen wir 2 mal einen <strong>20€</strong> Gutschein!</p>
  <p class="promo-copy" style="top:343px">So kannst du mitmachen:</p>
  <p class="promo-copy" style="top:382px">Gib unserer Seite einen Daumen hoch.</p>
  <p class="promo-copy" style="top:420px">Like and poste diesen Beitrag auf deinen Profil und sehr wichtig!!!</p>
  <p class="promo-copy" style="top:458px">Markiert euren Lieblingsmenschen Derjenige, der es<br>verdient hat diesen Gewinn mit Dir zu Teilen.</p>
  <p class="promo-copy" style="top:516px">Ausgelost wird am Valenstag den <strong>14.01.2020</strong></p>
  <p class="promo-copy" style="top:554px">Unsere Gaststatte Zum Talhahn erwartet sie Gerne am<br>14.02.2020 mit einen besonderes Essen und mit einem<br>romantischen Ambiente.</p>

  <div class="gallery">
    <div class="gallery__photo photo--soup" role="img" aria-label="Photo of tomato soup in a green bowl"></div>
    <div class="gallery__photo photo--steak" role="img" aria-label="Photo of sliced steak with vegetables"></div>
    <div class="gallery__photo photo--dessert" role="img" aria-label="Photo of heart-shaped cookies with strawberries"></div>
  </div>
  <div class="promo-rule"></div>

  <div class="page__band"></div>
</section>

</body>
</html>
```